Website for Torvel Capital - investment banking firm

We have a corporate identity (thanks to Ranjita/41238) and want to extend that into a website design.  See the attached zipped files.
We have software folks in-house to do the coding.
See the attached Project Brief & Notes for more details.  Don't worry about the actual text - lorem ipsum will be fine.
The server will be Apache.
Thank you!
Desmond

```html
<!DOCTYPE html>
<html lang="en">
<head>
<meta charset="utf-8">
<title>Torvel Capital</title>
<link href="https://fonts.googleapis.com/css2?family=Open+Sans:wght@400;600;700&display=swap" rel="stylesheet">
<style>
:root{
  --ink:#333;
  --muted:#666;
  --navy:#1f3f7a;
  --blue:#2a6fb5;
  --link:#2a7fc4;
  --green:#3a9a3a;
  --rule:#e2e2e2;
  --pink:#e0588c;
  --teal:#2fb6c9;
  --orange:#e5744b;
  --footer:#363941;
  --footer-deep:#26282e;
  --footer-text:#c9ccd2;
}
*{box-sizing:border-box;margin:0;padding:0}
html,body{width:1200px;height:2774px;overflow:hidden;background:#fff}
body{font-family:"Open Sans",Arial,sans-serif;color:var(--ink);position:relative}
.abs{position:absolute}
/* header */
.site-header{left:0;top:0;width:1200px;height:50px;background:#fff;border-bottom:1px solid var(--rule)}
.brand{left:222px;top:6px;display:flex;align-items:center;gap:10px}
.brand-mark{width:36px;height:36px;background:var(--navy)}
.brand-name{font-size:26px;font-weight:600;color:var(--navy);letter-spacing:.5px}
.main-nav{right:222px;top:18px;display:flex;gap:22px;font-size:12px;color:#444}
/* hero */
.hero{left:0;top:50px;width:1200px;height:455px;background:linear-gradient(100deg,#dfe3e6 0%,#c9ced3 35%,#b8bec4 60%,#8e959d 100%)}
.hero-title{left:278px;top:208px;font-size:40px;color:#111}
.hero-sub{left:332px;top:268px;font-size:22px;color:#fff}
.hero-arrow{top:248px;width:38px;height:38px;background:#3a3a3a;color:#fff;font-size:20px;line-height:38px;text-align:center}
/* client strip */
.clients{left:222px;top:560px;width:760px;height:76px;border-top:1px solid var(--rule);border-bottom:1px solid var(--rule);display:flex;align-items:center;justify-content:space-between;padding:0 2px}
.strip-btn{width:20px;height:20px;background:#333;color:#fff;font-size:11px;line-height:20px;text-align:center}
.client-names{display:flex;gap:38px;font-size:22px;font-weight:600;color:#555}
/* sections */
h2.section-title{font-size:22px;font-weight:400;color:#333;position:absolute}
.rule{left:222px;width:760px;height:1px;background:var(--rule)}
.feature{top:745px;width:240px}
.feature h3{font-size:14px;font-weight:400;margin-left:52px;margin-bottom:6px}
.feature p{font-size:11.5px;line-height:18px;color:#555}
.feature svg{position:absolute;left:0;top:0}
.dial{top:940px;width:134px;height:134px}
/* showcase */
.showcase{left:222px;top:1180px;width:495px;height:316px;border:1px solid var(--rule)}
.showcase-img{left:18px;top:17px;width:457px;height:198px;border:1px solid #ccc;background:linear-gradient(180deg,#fafbfd,#dfe8f3 70%,#c8d8ec)}
.showcase h4{left:18px;top:240px;font-size:15px;font-weight:400}
.showcase p{left:18px;top:264px;width:450px;font-size:11px;line-height:18px;color:#777}
.ticker{left:232px;top:1512px;display:flex;gap:14px}
.ticker h5{font-size:13px;font-weight:400}
.ticker p{font-size:11px;color:var(--link)}
.pager{left:685px;top:1510px;font-size:13px;color:var(--link);letter-spacing:8px}
.checklist{left:753px;top:1182px;list-style:none}
.checklist li{height:30px;font-size:13.5px;display:flex;align-items:center;gap:8px}
/* testimonials */
.quote-box{left:222px;top:1738px;width:233px;height:207px;background:#f4f4f4;padding:18px 12px;font-size:11px;line-height:22.5px;color:#333}
.quote-author{left:230px;top:1960px;display:flex;gap:12px;align-items:center}
.avatar{width:44px;height:44px;border-radius:50%;background:linear-gradient(135deg,#b89a84,#6e5a4e)}
.quote-author h5{font-size:13px;font-weight:400}
.quote-author p{font-size:11px;color:var(--link)}
.timeline-line{left:524px;top:1763px;width:1px;height:290px;background:var(--rule)}
.tl-icon{left:484px;width:80px;height:80px;border-radius:50%;border:1px solid #ddd;background:#fff}
.tl-text{left:586px;width:400px}
.tl-text h4{font-size:17px;font-weight:400;margin-bottom:8px}
.tl-text p{font-size:11.5px;line-height:18px;color:#555}
/* stats */
.stat{top:2185px;width:200px;text-align:center}
.stat b{display:block;font-size:46px;font-weight:400;line-height:56px}
.stat span{font-size:10px;color:#666}
/* footer */
.site-footer{left:0;top:2314px;width:1200px;height:427px;background:linear-gradient(180deg,var(--footer),#2f3239)}
.footer-title{font-size:16px;font-weight:400;color:#fff}
.f-text{color:var(--footer-text);font-size:10px;line-height:16px}
.socials{left:222px;top:2372px;display:flex;gap:6px}
.socials i{width:22px;height:22px;background:#4b86c6;display:block}
.field{height:18px;background:#2a2c32;border:1px solid #1f2126;width:170px}
.f-label{font-size:10px;color:#ddd}
.submit{left:222px;top:2608px;width:60px;height:22px;background:#2e7bc2;color:#fff;font-size:10px;text-align:center;line-height:22px}
.post{left:748px;width:240px;display:flex;gap:12px}
.post-thumb{width:50px;height:50px;background:linear-gradient(135deg,#d9d4cc,#7d736a)}
.f-divider{width:230px;height:1px;background:#4a4d55}
.bottom-bar{left:0;top:2741px;width:1200px;height:33px;background:var(--footer-deep);font-size:10px;color:#999}
</style>
</head>
<body>

<header class="site-header abs">
  <div class="brand abs"><span class="brand-mark"></span><span class="brand-name">Torvel Capital</span></div>
  <nav class="main-nav abs"><span>Home</span><span>About</span><span>Services</span><span>Current Engagements</span><span>Completed Transactions</span></nav>
</header>

<section class="hero abs" role="img" aria-label="Photo of business people in a bright office, a smiling man on a phone at right"></section>
<div class="hero-title abs">Lorem Ipsum</div>
<div class="hero-sub abs">Ipsum lorem</div>
<div class="hero-arrow abs" style="left:0">&#10094;</div>
<div class="hero-arrow abs" style="right:0;background:transparent">&#10095;</div>

<div class="clients abs">
  <span class="strip-btn">&#9664;</span>
  <div class="client-names"><span>Kestra</span><span>Volnix</span><span>Maribel</span><span>Ostrand</span><span>Quillon</span><span>Maribel</span></div>
  <span class="strip-btn">&#9654;</span>
</div>

<h2 class="section-title" style="left:222px;top:690px">Why Choose Us</h2>
<div class="feature abs" style="left:222px">
  <svg width="36" height="28" viewBox="0 0 36 28"><ellipse cx="14" cy="11" rx="13" ry="9" fill="var(--blue)"/><path d="M6 17 L3 25 L13 19Z" fill="var(--blue)"/><ellipse cx="24" cy="16" rx="10" ry="7" fill="#5b9bd8"/></svg>
  <h3>Lorem Ipsum</h3>
  <p>Lorem ipsum Lorem ipsum Lorem ipsum Lorem Ipsum Lorem ipsum Lorem Ipsum Lorem Ipsum Lorem ipsum Lorem ipsum Lorem ipsum Lorem Ipsum Lorem ipsum Lorem Ipsum Lorem ipsum Lorem ipsum Lorem</p>
</div>
<div class="feature abs" style="left:485px">
  <svg width="36" height="30" viewBox="0 0 36 30"><rect x="2" y="2" width="32" height="20" rx="2" fill="none" stroke="#d33b3b" stroke-width="4"/><rect x="14" y="22" width="8" height="4" fill="#d33b3b"/><rect x="9" y="26" width="18" height="3" fill="#d33b3b"/></svg>
  <h3>Lorem Ipsum</h3>
  <p>Lorem ipsum Lorem ipsum Lorem ipsum Lorem Ipsum Lorem ipsum Lorem Ipsum Lorem Ipsum Lorem ipsum Lorem ipsum Lorem ipsum Lorem Ipsum Lorem ipsum Lorem Ipsum Lorem ipsum Lorem ipsum Lorem</p>
</div>
<div class="feature abs" style="left:748px">
  <svg width="36" height="28" viewBox="0 0 36 28"><path d="M11 5 L3 14 L11 23 M25 5 L33 14 L25 23" fill="none" stroke="var(--blue)" stroke-width="3"/><path d="M21 3 L15 25" stroke="#555" stroke-width="2.5"/></svg>
  <h3>Lorem Ipsum</h3>
  <p>Lorem ipsum Lorem ipsum Lorem ipsum Lorem Ipsum Lorem ipsum Lorem Ipsum Lorem Ipsum Lorem ipsum Lorem ipsum Lorem ipsum Lorem Ipsum Lorem ipsum Lorem Ipsum Lorem ipsum Lorem ipsum Lorem</p>
</div>
<div class="rule abs" style="top:902px"></div>

<svg class="dial abs" style="left:271px" viewBox="0 0 134 134">
  <circle cx="67" cy="67" r="63" fill="none" stroke="#eee" stroke-width="6"/>
  <path d="M67 4 A63 63 0 1 1 14 101" fill="none" stroke="var(--navy)" stroke-width="6"/>
  <path d="M48 62 h20 v-9 l14 14 l-14 14 v-9 h-20z" fill="#222"/><path d="M74 50 h14 v34 h-14" fill="none" stroke="#222" stroke-width="4"/>
</svg>
<svg class="dial abs" style="left:532px" viewBox="0 0 134 134">
  <circle cx="67" cy="67" r="63" fill="none" stroke="#eee" stroke-width="6"/>
  <path d="M67 4 A63 63 0 1 1 4 67" fill="none" stroke="var(--navy)" stroke-width="6"/>
  <text x="67" y="74" text-anchor="middle" font-family="Open Sans, sans-serif" font-size="21" fill="#333">75%</text>
</svg>
<svg class="dial abs" style="left:794px" viewBox="0 0 134 134">
  <circle cx="67" cy="67" r="63" fill="none" stroke="var(--navy)" stroke-width="6"/>
  <path d="M50 46 v46" stroke="#222" stroke-width="4"/><path d="M52 48 q18 -8 34 0 v22 q-16 -8 -34 0z" fill="#222"/><path d="M60 50 h8 v8 h-8z M76 58 h8 v8 h-8z M68 58 h8 v8 h-8z" fill="#fff"/>
</svg>
<div class="rule abs" style="top:1124px"></div>

<section class="showcase abs">
  <div class="showcase-img abs" role="img" aria-label="Illustration of small blue figures building a rising bar chart"></div>
  <h4 class="abs">LOREM IPSUM</h4>
  <p class="abs">Lorem ipsum lorem ipsum lorem ipsum lorem ipsum lorem ipsum lorem ipsum lorem ipsum lorem ipsum lorem ipsum lorem ipsum lorem ipsum</p>
</section>
<div class="ticker abs">
  <svg width="36" height="34" viewBox="0 0 36 34"><path d="M3 18 L13 29 L33 4" fill="none" stroke="var(--green)" stroke-width="6"/></svg>
  <div><h5>LOREM IPSUM</h5><p>Lorem ipsum lorem ipsum lorem ipsum lorem</p></div>
</div>
<div class="pager abs">&#8249;&#8250;</div>
<ul class="checklist abs">
  <li><svg width="14" height="12"><path d="M1 6 L5 10 L13 1" fill="none" stroke="var(--green)" stroke-width="2.5"/></svg>Lorem Ipsum Lorem Ipsum</li>
  <li><svg width="14" height="12"><path d="M1 6 L5 10 L13 1" fill="none" stroke="var(--green)" stroke-width="2.5"/></svg>Lorem Ipsum Lorem Ipsum</li>
  <li><svg width="14" height="12"><path d="M1 6 L5 10 L13 1" fill="none" stroke="var(--green)" stroke-width="2.5"/></svg>Lorem Ipsum Lorem Ipsum</li>
  <li><svg width="14" height="12"><path d="M1 6 L5 10 L13 1" fill="none" stroke="var(--green)" stroke-width="2.5"/></svg>Lorem Ipsum Lorem Ipsum</li>
  <li><svg width="14" height="12"><path d="M1 6 L5 10 L13 1" fill="none" stroke="var(--green)" stroke-width="2.5"/></svg>Lorem Ipsum Lorem Ipsum</li>
  <li><svg width="14" height="12"><path d="M1 6 L5 10 L13 1" fill="none" stroke="var(--green)" stroke-width="2.5"/></svg>Lorem Ipsum Lorem Ipsum</li>
  <li><svg width="14" height="12"><path d="M1 6 L5 10 L13 1" fill="none" stroke="var(--green)" stroke-width="2.5"/></svg>Lorem Ipsum Lorem Ipsum</li>
  <li><svg width="14" height="12"><path d="M1 6 L5 10 L13 1" fill="none" stroke="var(--green)" stroke-width="2.5"/></svg>Lorem Ipsum Lorem Ipsum</li>
  <li><svg width="14" height="12"><path d="M1 6 L5 10 L13 1" fill="none" stroke="var(--green)" stroke-width="2.5"/></svg>Lorem Ipsum Lorem Ipsum</li>
  <li><svg width="14" height="12"><path d="M1 6 L5 10 L13 1" fill="none" stroke="var(--green)" stroke-width="2.5"/></svg>Lorem Ipsum Lorem Ipsum</li>
  <li><svg width="14" height="12"><path d="M1 6 L5 10 L13 1" fill="none" stroke="var(--green)" stroke-width="2.5"/></svg>Lorem Ipsum Lorem Ipsum</li>
  <li><svg width="14" height="12"><path d="M1 6 L5 10 L13 1" fill="none" stroke="var(--green)" stroke-width="2.5"/></svg>Lorem Ipsum Lorem Ipsum</li>
  <li><svg width="14" height="12"><path d="M1 6 L5 10 L13 1" fill="none" stroke="var(--green)" stroke-width="2.5"/></svg>Lorem Ipsum Lorem Ipsum</li>
  <li><svg width="14" height="12"><path d="M1 6 L5 10 L13 1" fill="none" stroke="var(--green)" stroke-width="2.5"/></svg>Lorem Ipsum Lorem Ipsum</li>
</ul>
<div class="rule abs" style="top:1637px"></div>

<h2 class="section-title" style="left:222px;top:1690px">What Our Clients Say</h2>
<div class="quote-box abs">Lorem Ipsum lorem ipsum lorem ipsum lorem ipsum lorem ipsum lorem ipsum lorem ipsum lorem ipsum lorem ipsum lorem ipsum lorem ipsum lorem ipsum lorem ipsum lorem ipsum lorem ipsum lorem ipsum lorem ipsum lorem ipsum lorem ipsum lorem ipsum lorem ipsum lorem ipsum...</div>
<div class="quote-author abs">
  <div class="avatar" role="img" aria-label="Client portrait photo"></div>
  <div><h5>LOREM IPSUM</h5><p>Lorem ipsum lorem ipsum</p></div>
  <span style="color:var(--link);font-size:13px;letter-spacing:8px;margin-left:8px;margin-top:-18px">&#8249;&#8250;</span>
</div>
<div class="timeline-line abs"></div>
<svg class="tl-icon abs" style="top:1723px" viewBox="0 0 80 80"><rect x="28" y="30" width="24" height="22" fill="none" stroke="#888" stroke-width="2"/><path d="M28 36 h24 M34 27 v6 M46 27 v6 M33 42 h4 M39 42 h4 M45 42 h4 M33 47 h4 M39 47 h4" stroke="#888" stroke-width="2"/></svg>
<svg class="tl-icon abs" style="top:1847px" viewBox="0 0 80 80"><path d="M30 52 L32 44 L48 28 L54 34 L38 50Z" fill="#888"/></svg>
<svg class="tl-icon abs" style="top:1973px" viewBox="0 0 80 80"><rect x="27" y="30" width="26" height="17" fill="none" stroke="#888" stroke-width="2.5"/><path d="M36 51 h8 M40 47 v4" stroke="#888" stroke-width="2.5"/></svg>
<div class="tl-text abs" style="top:1724px"><h4>Lorem Ipsum</h4><p>Lorem Ipsum Lorem Ipsum Lorem Ipsum Lorem Ipsum Lorem Ipsum Lorem Ipsum Lorem Ipsum Lorem Ipsum</p></div>
<div class="tl-text abs" style="top:1848px"><h4>Lorem Ipsum</h4><p>Lorem Ipsum Lorem Ipsum Lorem Ipsum Lorem Ipsum Lorem Ipsum Lorem Ipsum Lorem Ipsum Lorem Ipsum Lorem Ipsum Lorem Ipsum</p></div>
<div class="tl-text abs" style="top:1974px"><h4>Lorem Ipsum</h4><p>Lorem Ipsum Lorem Ipsum Lorem Ipsum Lorem Ipsum Lorem Ipsum Lorem Ipsum Lorem Ipsum Lorem Ipsum</p></div>
<div class="rule abs" style="top:2084px"></div>

<div class="stat abs" style="left:203px"><b style="color:var(--pink)">798</b><span>Positive Feedback</span></div>
<div class="stat abs" style="left:400px"><b style="color:var(--teal)">542</b><span>Average cost per hour</span></div>
<div class="stat abs" style="left:597px"><b style="color:var(--teal)">652</b><span>Projects completed</span></div>
<div class="stat abs" style="left:794px"><b style="color:var(--orange)">856</b><span>Something Special</span></div>

<footer class="site-footer abs"></footer>
<h4 class="footer-title abs" style="left:222px;top:2344px">Keep In Touch</h4>
<div class="socials abs"><i></i><i></i><i></i><i></i><i></i></div>
<h4 class="footer-title abs" style="left:222px;top:2428px">Connect With Us!</h4>
<div class="field abs" style="left:222px;top:2462px"></div><span class="f-label abs" style="left:400px;top:2464px">Name *</span>
<div class="field abs" style="left:222px;top:2492px"></div><span class="f-label abs" style="left:400px;top:2494px">Email *</span>
<div class="field abs" style="left:222px;top:2520px;width:222px;height:80px"></div>
<div class="submit abs">Submit</div>

<h4 class="footer-title abs" style="left:485px;top:2344px">Contact Us</h4>
<div class="f-text abs" style="left:485px;top:2376px">&#9742;&nbsp; +00 123 456 7890<br>&#9993;&nbsp; <span style="color:var(--link)">hello@torvelcapital.com</span><br>&#9679;&nbsp; Lorem ipsum lorem ipsum<br>&nbsp;&nbsp;&nbsp;&nbsp;Lorem ipsum lorem ipsum</div>
<div class="f-divider abs" style="left:485px;top:2448px"></div>
<h4 class="footer-title abs" style="left:485px;top:2486px">Recent Tweets</h4>
<div class="f-text abs" style="left:485px;top:2518px;width:235px">
  <p><span style="color:var(--link)">about 120 days ago</span> Fresh Corner Deli Bar using Lumen Theme lorem ipsum lorem ipsum, nice to see it</p>
  <p style="margin-top:8px"><span style="color:var(--link)">about 122 days ago</span> Thanks to all users who shared so many ideas and testing. You are great and I am truly thankful for your support</p>
  <p style="margin-top:8px"><span style="color:var(--link)">about 125 days ago</span> Lumen Theme submitted to Marketly for review. The long beta process is over</p>
</div>

<h4 class="footer-title abs" style="left:748px;top:2344px">Popular Posts</h4>
<div class="post abs" style="top:2376px"><div class="post-thumb" role="img" aria-label="Post thumbnail photo"></div><div class="f-text"><span style="color:var(--link)">Lorem ipsum lorem ipsum</span><br>October 30, 2015</div></div>
<div class="f-divider abs" style="left:748px;top:2436px"></div>
<div class="post abs" style="top:2446px"><div class="post-thumb" role="img" aria-label="Post thumbnail photo"></div><div class="f-text"><span style="color:var(--link)">Lorem ipsum lorem ipsum</span><br>October 30, 2015</div></div>
<div class="f-divider abs" style="left:748px;top:2506px"></div>

<div class="bottom-bar abs">
  <span class="abs" style="left:222px;top:10px">Copyright &copy; 2014. All Rights Reserved.</span>
  <span class="abs" style="left:552px;top:10px;letter-spacing:1px">&#8962; HOME &nbsp;&nbsp; ABOUT &nbsp;&nbsp; SERVICES &nbsp;&nbsp; CURRENT ENGAGEMENTS &nbsp;&nbsp; COMPLETED TRANSACTIONS</span>
</div>

</body>
</html>
```